QV - menu design

Hi,

We require elegant menu design for upscale restaurant. Please find attached the logo and the menu items for your reference.

for inspiration, this is a good website: -
http://www.platewhisper.example/bellfoldnotes/about.php

We are very much open for Menu Size suggestions.

unfortunately the place is going under renovation, we don't have updated images to it. the closest look and feel to our place is http://varnelo.example ..

we are also open for creative options on the shape, the styles, etc. as long as it represents the fine dine feel ...

Thanks ...

Dear All,

We wouldlike to extend our apology for not being able to provide feedbacks on everysingle design. We were extremely busy and we have multiple contests opensimultaneously which makes the process even harder.

However,we would like to thank you all for the efforts you have put into designingour menu. It is very much appreciated …

We wishyou all success in your design ventures and we are quite positive that we willbe working with many of you on many projects in the soon future. 

Thanks & Regards,

TLG Team...

 

 

 

Industry/Entity Type

Restaurant

Requirements
Must have
• Please ensure that there are 'some' images in the menu ... this is very important.
Should not have
• IMPORTANT: -

1. Please DO NOT insert any currency sign to the menu
2. Please keep the prices of the menu at the end of the menu items descriptions NOT beside the menu item names. The font of the price should be similar to the menu item description and please DO NOT bold the numbers. the prices should be subtle.

Thank you ...

```html
<!DOCTYPE html>
<html lang="en">
<head>
<meta charset="utf-8">
<title>QV Café – Menu</title>
<link rel="stylesheet" href="https://fonts.googleapis.com/css2?family=Dosis:wght@300;400&family=Libre+Baskerville:ital,wght@0,700;1,400;1,700&family=Crimson+Pro:ital,wght@1,400;1,700&display=swap">
<style>
  :root {
    --paper: #ffffff;
    --ink: #1f1f1f;
    --heading: #4d4d4d;
    --accent: #a8835a;
    --rule: #a9a9a9;
    --art-a: #e4dccd;
    --art-b: #c8b89c;
  }
  * { box-sizing: border-box; margin: 0; padding: 0; }
  html, body { width: 1200px; height: 1200px; overflow: hidden; background: var(--paper); }
  .menu { position: relative; width: 1200px; height: 1200px; color: var(--ink);
    font-family: "Crimson Pro", Georgia, serif; font-style: italic; font-size: 17px; line-height: 21px; }

  .brand { position: absolute; left: 97px; top: 70px; width: 230px; text-align: center;
    font-family: "Dosis", sans-serif; font-weight: 300; color: var(--ink); letter-spacing: 10px; }
  .brand__name { font-size: 64px; line-height: 70px; }
  .brand__sub { font-size: 18px; letter-spacing: 8px; margin-top: 4px; }

  .art { position: absolute; border-radius: 50%; }
  .art--roast { left: 672px; top: 6px; width: 200px; height: 150px;
    background: radial-gradient(ellipse at 50% 45%, var(--art-b), var(--art-a) 60%, transparent 72%); }
  .art--pasta { left: 108px; top: 1002px; width: 205px; height: 150px;
    background: radial-gradient(ellipse at 50% 55%, var(--art-b), var(--art-a) 58%, transparent 72%); }

  .rule-h, .rule-v { position: absolute; border: 0 dotted var(--rule); }
  .rule-h { border-top-width: 2px; }
  .rule-v { border-left-width: 2px; }

  .section-title { font-family: "Dosis", sans-serif; font-weight: 300; font-style: normal;
    color: var(--heading); font-size: 36px; letter-spacing: 2px; line-height: 40px; text-align: center; }

  .section { position: absolute; text-align: center; }
  .section--first { left: 427px; top: 222px; width: 773px; }
  .section--apps { left: 0; top: 364px; width: 425px; }
  .section--main { left: 427px; top: 584px; width: 340px; }
  .section--rotis { left: 769px; top: 584px; width: 431px; }

  .items { list-style: none; }
  .section--first .items { margin-top: 14px; }
  .section--first .item { margin-bottom: 9px; }
  .section--apps .items { margin-top: 38px; }
  .section--apps .item { margin-bottom: 19px; }
  .section--main .items { margin-top: 40px; }
  .section--main .item { margin-bottom: 19px; }
  .section--rotis .items { margin-top: 40px; }
  .section--rotis .item { margin-bottom: 12px; }

  .item__name { font-family: "Libre Baskerville", serif; font-weight: 700; font-style: italic; font-size: 15px; }
  .item__name--course { font-family: "Libre Baskerville", serif; font-weight: 700; font-style: normal;
    color: var(--accent); font-size: 19px; line-height: 28px; display: block; }
  .item__price { font-weight: 400; }
</style>
</head>
<body>
<main class="menu">
  <header class="brand">
    <div class="brand__name">QV</div>
    <div class="brand__sub">CAFÉ</div>
  </header>

  <div class="art art--roast" role="img" aria-label="Engraved-style illustration of a roast chicken on a platter"></div>
  <div class="art art--pasta" role="img" aria-label="Engraved-style illustration of a plate of filled pasta"></div>

  <div class="rule-h" style="left:425px; top:215px; width:775px;"></div>
  <div class="rule-v" style="left:425px; top:215px; height:985px;"></div>
  <div class="rule-h" style="left:0; top:353px; width:425px;"></div>
  <div class="rule-h" style="left:0; top:408px; width:425px;"></div>
  <div class="rule-h" style="left:425px; top:580px; width:775px;"></div>
  <div class="rule-v" style="left:767px; top:580px; height:620px;"></div>
  <div class="rule-h" style="left:425px; top:633px; width:775px;"></div>

  <section class="section section--first">
    <h2 class="section-title">FIRST COURSES</h2>
    <ul class="items">
      <li class="item"><span class="item__name">Tagliatelle served on a whole Lobster</span> with fresh Asparagus tops,<br>cherry tomato and crispy beef bacon. <span class="item__price">249</span></li>
      <li class="item"><span class="item__name">Whole wheat Maltagliati</span> with Porcini mushrooms and Parmesan cheese cream. <span class="item__price">99</span></li>
      <li class="item"><span class="item__name">Penne pasta with fresh broccoli,</span> Taleggio cheese cream, toasted almonds and fresh chili</li>
      <li class="item"><span class="item__name">Spaghetti</span> with a smooth and creamy sauce and juicy chicken breast</li>
      <li class="item"><span class="item__name">Fettuccine with fresh salmon,</span> saffron and toasted pine nuts</li>
      <li class="item"><span class="item__name">Seaweed tagliatelle</span> with king scallops and poached egg</li>
      <li class="item"><span class="item__name">Risotto with Prawns,</span> green peas and beetroot reduction. <span class="item__price">149</span></li>
      <li class="item"><span class="item__name">Risotto “Primavera”</span> with fresh seasonal vegetables served on a squash cream. <span class="item__price">69</span></li>
      <li class="item"><span class="item__name">Risotto with porcini mushrooms</span> and garlic chips</li>
    </ul>
  </section>

  <section class="section section--apps">
    <h2 class="section-title">APPETIZERS</h2>
    <ul class="items">
      <li class="item"><span class="item__name">Fresh tomato and mozzarella</span> terrine with<br>basil sauce, black olives and fresh capers.</li>
      <li class="item"><span class="item__name">Fresh salmon sashimi</span><br>seared in olive oil with spring and red onions,<br>orange zest and fresh sweet chili. <span class="item__price">79</span></li>
      <li class="item"><span class="item__name">Duck Foie Gras</span> terrine with<br>toasted Pan Brioche and red onion jam spheres. <span class="item__price">124</span></li>
      <li class="item"><span class="item__name">Selection of vegetables</span> stuffed with<br>fresh spinach, goat cheese and fresh mint<br>on a garlic-tomato coulis. <span class="item__price">93</span></li>
      <li class="item"><span class="item__name">Grilled Octopus</span> with bell peppers,<br>roasted tofu, lemon zest and sweet n’ sour<br>soy drops. <span class="item__price">99</span></li>
      <li class="item"><span class="item__name">Sea Scallops “au gratin”</span> with garlic chips,<br>walnut cream and truffle oil. <span class="item__price">176</span></li>
      <li class="item"><span class="item__name">Irish Beef “Carpaccio”</span> on a<br>Bagna Cauda sauce and truffle slices, with toasted<br>pine nuts and seasonal fresh salad. <span class="item__price">79</span></li>
      <li class="item"><span class="item__name">Prawn</span> with white chocolate sauce,<br>thyme croutons, fresh celery on a<br>Vitellotte potato cream. <span class="item__price">89</span></li>
    </ul>
  </section>

  <section class="section section--main">
    <h2 class="section-title">MAIN COURSES</h2>
    <ul class="items">
      <li class="item"><span class="item__name">Grilled beef tenderloin</span> with<br>balsamic sauce, mashed potatoes and<br>grilled pumpkin. <span class="item__price">149</span></li>
      <li class="item"><span class="item__name">Chicken supreme</span> stuffed with<br>Fontina cheese, spinach and black olives<br>in a crispy panko crust served on<br>aborigine “Caponata”. <span class="item__price">139</span></li>
      <li class="item"><span class="item__name">Grilled fresh Salmon</span> dusted in<br>herbs with seasonal sautéed vegetables with<br>sesame and light soy sauce. <span class="item__price">14</span></li>
      <li class="item"><span class="item__name">Sea Bass</span> crumble with smashed potato<br>and Zucchini ratatouille. <span class="item__price">159</span></li>
      <li class="item"><span class="item__name">The Paella,</span> traditional Spanish seafood<br>and chicken dish, served with saffron rice<br>and green peas. <span class="item__price">229</span></li>
      <li class="item"><span class="item__name">Stuffed calamari</span> with breadcrumbs,<br>black olives, green peas served on a semolina<br>crouton and fresh tomato sauté.</li>
    </ul>
  </section>

  <section class="section section--rotis">
    <h2 class="section-title">THE ROTISSERIE</h2>
    <ul class="items">
      <li class="item"><span class="item__name--course">Spring chicken</span>Marinated in fresh rosemary, lemon zest, garlic and<br>black pepper grains served with baked potatoes,<br>herb butter, sage rice and our lemon pickle sauce. <span class="item__price">139</span></li>
      <li class="item"><span class="item__name--course">Baby Duck</span>Roasted in Banana leaves and fresh lemongrass served<br>with potatoes “Au gratin”, sautéed Foie Gras steak,<br>red onion rings and toasted orange sauce. <span class="item__price">149</span></li>
      <li class="item"><span class="item__name--course">Boneless Lamb</span>Stuffed with black olives and dried plum, served<br>on sautéed fresh spinach, Toasted pine nuts, garlic<br>breadcrumbs and thyme smashed potatoes. <span class="item__price">149</span></li>
      <li class="item"><span class="item__name--course">Beef Sirloin</span>Marinated in spring onions, garlic and<br>mustard, served on rosemary potatoes, Vichy carrots<br>and green pepper sauce. <span class="item__price">149</span></li>
      <li class="item"><span class="item__name--course">Chicken Shawarma</span>Served in the inimitable QV style with<br>garlic sauce, cucumber and tomato pickles<br>and three peppers coulis. <span class="item__price">75</span></li>
    </ul>
  </section>
</main>
</body>
</html>
```